Promotional Poster for Music Achievement Program

I need a vertical 11x17 poster designed for a new program called Bright Steps Music Achievement Program. The poster will be displayed in the lesson rooms and lobbies of music schools who use this program. The main headline of the flyer should be "Ask your teacher about Bright Steps" And then the additional text should be "Love your lessons and practice like never before with 10 levels of achievement!" I would like to use the logo on the flyer, which I uploaded here. In terms of artwork/design, I am looking for a fun, but clean feel. The purpose of the program is for students to progress through ten levels of achievement as they climb higher and higher to mastery of their instrument at level 10, so a feel of climbing, leveling up, or advancing would be good. And of course, this is a music program, so any musical artwork involved would make sense. But again - nothing too busy or overwhelming!

Target Market(s)

Parents waiting in the lobby of a music school.

Industry/Entity Type

Promotional

Colors

Designer to choose colors to be used in the design.

Requirements
Must have
• - Bright Steps logo
• - This headline: Ask your teacher about Bright Steps
• - This additional text: Love your lessons and practice like never before with 10 levels of achievement!
Nice to have
• In terms of artwork/design, I am looking for a fun, but clean feel. The purpose of the program is for students to progress through ten levels of achievement as they climb higher and higher to mastery of their instrument at level 10, so a feel of climbing, leveling up, or advancing would be good. And of course, this is a music program, so any musical artwork involved would make sense. But again - nothing too busy or overwhelming!
Should not have
• Should not be too busy.

```html
<!DOCTYPE html>
<html lang="en">
<head>
<meta charset="utf-8">
<title>Bright Steps Music Achievement Program – Poster</title>
<link rel="stylesheet" href="https://fonts.googleapis.com/css2?family=Arimo:wght@400&family=Montserrat:wght@700&family=Nunito+Sans:wght@900&family=Oswald:wght@300&display=swap">
<style>
  :root {
    --backdrop: #cddd2b;
    --paper: #f6f9e0;
    --lime: #c6d72b;
    --orange: #f9b03f;
    --red: #ec1c24;
    --ink: #000000;
    --console-tone: #e3e9c2;
  }
  html, body {
    margin: 0;
    padding: 0;
    width: 1200px;
    height: 1200px;
    overflow: hidden;
    background: var(--backdrop);
  }
  .canvas {
    position: relative;
    width: 1200px;
    height: 1200px;
  }
  .poster {
    position: absolute;
    left: 264px;
    top: 134px;
    width: 620px;
    height: 958px;
    background: var(--paper);
    overflow: hidden;
  }
  .console-photo {
    position: absolute;
    left: 110px;
    top: 700px;
    width: 510px;
    height: 258px;
    background: radial-gradient(ellipse at 65% 75%, var(--console-tone) 0%, rgba(227,233,194,0.6) 45%, rgba(246,249,224,0) 80%);
  }
  .staff {
    position: absolute;
    display: flex;
    flex-direction: column;
    gap: 12px;
  }
  .staff-top { right: 40px; top: 48px; width: 220px; }
  .staff-bottom { left: 40px; bottom: 48px; width: 220px; }
  .staff-line { height: 5px; width: 100%; }
  .line-lime { background: var(--lime); }
  .line-orange { background: var(--orange); }
  .line-red { background: var(--red); }
  .line-ink { background: var(--ink); }

  .headline {
    position: absolute;
    left: 182px;
    top: 262px;
    width: 340px;
    margin: 0;
    font-family: "Nunito Sans", Verdana, sans-serif;
    font-weight: 900;
    font-size: 40px;
    line-height: 38px;
    color: var(--red);
    text-align: right;
    transform: rotate(-3deg);
    transform-origin: left top;
  }
  .headline span { display: block; }
  .headline .about { padding-right: 104px; }

  .brand {
    position: absolute;
    left: 24px;
    top: 340px;
    display: flex;
    align-items: center;
    gap: 22px;
  }
  .brand-mark {
    width: 56px;
    height: 56px;
    background: var(--red);
  }
  .brand-name {
    font-family: "Montserrat", Arial, sans-serif;
    font-weight: 700;
    font-size: 66px;
    line-height: 1;
    color: var(--ink);
    letter-spacing: -1px;
    white-space: nowrap;
  }

  .tagline {
    position: absolute;
    left: 120px;
    top: 516px;
    margin: 0;
    font-family: "Oswald", "Arial Narrow", sans-serif;
    font-weight: 300;
    font-size: 24px;
    line-height: 1;
    color: var(--ink);
    white-space: nowrap;
  }
  .levels {
    position: absolute;
    left: 110px;
    top: 534px;
    margin: 0;
    font-family: "Arimo", Arial, sans-serif;
    font-weight: 400;
    font-size: 102px;
    line-height: 1;
    color: var(--red);
    letter-spacing: -1.5px;
    white-space: nowrap;
  }
  .achievement {
    position: absolute;
    left: 248px;
    top: 632px;
    margin: 0;
    font-family: "Arimo", Arial, sans-serif;
    font-size: 34px;
    line-height: 1;
    color: var(--ink);
    white-space: nowrap;
  }
</style>
</head>
<body>
<div class="canvas">
  <div class="poster">
    <div class="console-photo" role="img" aria-label="Faded photograph of a studio mixing console"></div>

    <div class="staff staff-top" aria-hidden="true">
      <div class="staff-line line-lime"></div>
      <div class="staff-line line-orange"></div>
      <div class="staff-line line-red"></div>
      <div class="staff-line line-ink"></div>
    </div>
    <div class="staff staff-bottom" aria-hidden="true">
      <div class="staff-line line-lime"></div>
      <div class="staff-line line-orange"></div>
      <div class="staff-line line-red"></div>
      <div class="staff-line line-ink"></div>
    </div>

    <h1 class="headline"><span>Ask Your Teacher</span><span class="about">About</span></h1>

    <div class="brand">
      <div class="brand-mark"></div>
      <div class="brand-name">Bright Steps</div>
    </div>

    <p class="tagline">Love your lessons and practice like never before</p>
    <p class="levels">10 levels</p>
    <p class="achievement">of achievement!</p>
  </div>
</div>
</body>
</html>
```